Company or website name
- The Quillstone Movers and Storage
- Links to the website
- Quillstonehauling.com
- Describe your company and organization and target audience
- Residential and commercial moving and relocation service that needs a website redesign.
- The design should have the following
- I NEED THE WEBSITE TO BE SIMPLE AND STRAIGHT TO THE POINT...MAIN CONCERN IS THAT THEY FILL OUT INFORMATION TO GET QUOTE. SITE EXAMPLE THAT I LIKE IS ( WWW.MYPELDRAN.COM) https://www.orvikhaulage.com/

```html
<!DOCTYPE html>
<html lang="en">
<head>
<meta charset="utf-8">
<title>Quillstone Movers and Storage</title>
<link href="https://fonts.googleapis.com/css2?family=Lato:ital,wght@0,400;0,700;0,900;1,400&display=swap" rel="stylesheet">
<style>
:root{
  --brand:#535ef4;
  --ink:#1c1c1c;
  --muted:#555;
  --line:#d6d6d6;
  --soft:#f4f4f4;
  --star:#f7d116;
  --hero:#8f9aa3;
  --foot-bar:#e3e3e3;
}
*{box-sizing:border-box;margin:0;padding:0}
html,body{width:1200px;height:2335px;overflow:hidden;background:#fff}
body{font-family:"Lato",sans-serif;color:var(--ink)}
.page{position:relative;width:1200px;height:2335px;overflow:hidden}
.abs{position:absolute}
a{color:inherit;text-decoration:none}

/* header */
.site-header{position:absolute;left:0;top:0;width:1200px;height:93px;background:#fff}
.brand{position:absolute;left:86px;top:26px;display:flex;align-items:center;gap:10px}
.brand-mark{width:34px;height:34px;background:var(--ink)}
.brand-name{font-weight:900;font-size:30px;letter-spacing:3px;color:var(--ink);line-height:1}
.brand-tag{font-size:9px;font-weight:700;color:var(--ink);letter-spacing:.2px;margin-top:2px}
.main-nav{position:absolute;left:462px;top:39px;display:flex;gap:29px;font-size:15.5px;color:#333}
.main-nav .active{color:var(--brand)}
.nav-phone{display:flex;align-items:center;gap:5px}
.btn-request{position:absolute;left:961px;top:31px;width:140px;height:32px;border-radius:16px;background:#0d0d0d;color:#fff;font-size:12px;font-weight:700;display:flex;align-items:center;justify-content:center}

/* hero */
.hero-photo{position:absolute;left:0;top:93px;width:1200px;height:438px;background:linear-gradient(180deg,#b7c3cc 0%,#8d989d 45%,#5f6d4a 100%)}
.quote-panel{position:absolute;left:143px;top:415px;width:913px;height:169px;background:#fff;box-shadow:0 2px 8px rgba(0,0,0,.25)}
.quote-title{position:absolute;left:19px;top:22px;color:var(--brand);font-weight:900;font-size:16px}
.tabs{position:absolute;left:160px;top:15px;display:flex;border:1px solid var(--line);box-shadow:0 1px 3px rgba(0,0,0,.15)}
.tabs span{width:56px;height:31px;display:flex;align-items:center;justify-content:center;font-size:10px;color:#888;border-left:1px solid var(--line)}
.tabs span:first-child{border-left:0;color:#111;width:57px}
.field{position:absolute;width:220px}
.field label{display:block;font-size:11px;color:#111;margin-bottom:4px}
.field .input{height:28px;border:1px solid var(--line);border-radius:4px;box-shadow:0 1px 3px rgba(0,0,0,.12);font-size:9px;color:#999;padding:9px 8px}
.truck-icon{position:absolute;left:770px;top:78px;width:116px;height:36px}
.btn-quote{position:absolute;left:769px;top:122px;width:125px;height:32px;border-radius:16px;background:var(--brand);color:#fff;font-weight:900;font-size:13px;display:flex;align-items:center;justify-content:center}

/* section titles */
.section-title{position:absolute;color:var(--brand);font-weight:900;font-size:23px;letter-spacing:.8px}

/* services */
.service-card{position:absolute;top:671px;width:220px;height:251px;overflow:hidden}
.service-card .photo{position:absolute;inset:0}
.service-card .label{position:absolute;left:0;right:0;bottom:0;height:31px;background:rgba(20,20,30,.55);color:#fff;font-weight:900;font-size:12px;display:flex;align-items:center;justify-content:center}
.service-card.featured .photo{filter:brightness(.45)}
.featured-body{position:absolute;left:17px;top:134px;width:186px;color:#fff}
.featured-body h3{font-size:12px;font-weight:900;margin-bottom:7px}
.featured-body p{font-size:9px;line-height:12px;text-align:justify}
.featured-body .more{display:flex;justify-content:flex-end;gap:8px;margin-top:8px;font-size:10px;align-items:center}
.featured-body .more span{text-decoration:underline}
.round-arrow{position:absolute;width:34px;height:34px}
.btn-outline{position:absolute;left:497px;top:946px;width:157px;height:32px;border:1px solid #333;border-radius:4px;font-size:15px;letter-spacing:.6px;display:flex;align-items:center;justify-content:center}

/* about */
.about-box{position:absolute;left:86px;top:1064px;width:1014px;height:374px;background:#fff;box-shadow:0 1px 8px rgba(0,0,0,.25)}
.about-list{position:absolute;left:30px;top:26px;width:495px;list-style:none}
.about-list li{display:flex;gap:11px;font-size:14.2px;line-height:18px;color:#333;margin-bottom:12px;text-align:justify;letter-spacing:.2px}
.about-list li svg{flex:0 0 32px;margin-top:-1px}
.about-list li p{flex:1}
.about-link{position:absolute;left:72px;top:323px;font-size:15px;text-decoration:underline;color:#111}
.pinned{position:absolute;left:564px;top:29px;width:416px;height:314px;background:#fff;box-shadow:0 1px 6px rgba(0,0,0,.35);padding:6px}
.pinned .photo{width:100%;height:100%;background:linear-gradient(135deg,#cfd6cf 0%,#c8a27a 45%,#e8e6e3 100%)}
.pin{position:absolute;top:-8px;width:12px;height:16px}

/* testimonials */
.testimonials{position:absolute;left:0;top:1483px;width:1200px;height:377px;background:var(--soft)}
.t-card{position:absolute;top:101px;width:375px;height:218px;background:#fff;box-shadow:0 8px 20px rgba(0,0,0,.12)}
.t-card::before{content:"";position:absolute;left:-12px;top:20px;width:399px;height:185px;background:#fff;z-index:-1;box-shadow:0 0 3px rgba(0,0,0,.08)}
.t-quote{position:absolute;font-size:92px;font-weight:900;color:#bdbdbd;line-height:1;font-family:"Lato",sans-serif}
.t-stars{position:absolute;left:0;right:0;top:39px;display:flex;justify-content:center;gap:2px}
.t-text{position:absolute;left:40px;right:40px;top:72px;font-size:10.5px;font-style:italic;line-height:17px;text-align:center;color:#444}
.t-name{position:absolute;left:0;right:0;top:163px;text-align:center;font-size:10px;font-weight:900}
.t-role{position:absolute;left:0;right:0;top:177px;text-align:center;font-size:8.5px;color:#444}
.dark-arrow{position:absolute;width:34px;height:34px}

/* call to action */
.cta{position:absolute;left:0;top:1871px;width:1200px;height:185px;background:var(--brand);text-align:center}
.cta h2{position:absolute;left:0;right:0;top:38px;color:#fff;font-weight:900;font-size:30px;letter-spacing:1px}
.cta .btn-white{position:absolute;left:443px;top:97px;width:314px;height:44px;background:#fff;color:#111;font-size:19px;letter-spacing:.8px;display:flex;align-items:center;justify-content:center}

/* footer */
.site-footer{position:absolute;left:0;top:2056px;width:1200px;height:229px}
.foot-brand{position:absolute;left:88px;top:38px;display:flex;align-items:center;gap:6px}
.foot-brand .brand-mark{width:18px;height:18px}
.foot-brand .brand-name{font-size:18px;letter-spacing:2px}
.foot-company{position:absolute;left:87px;top:84px;font-size:14.5px;letter-spacing:.4px}
.foot-address{position:absolute;left:87px;top:124px;font-size:13.5px;line-height:19px;letter-spacing:.4px}
.foot-nav{position:absolute;left:413px;top:36px;list-style:none;font-size:14px;font-weight:700;letter-spacing:.6px}
.foot-nav li{margin-bottom:17px}
.foot-news-title{position:absolute;left:687px;top:35px;font-size:13.5px;font-weight:700;letter-spacing:.6px}
.foot-news-text{position:absolute;left:685px;top:72px;font-size:15px;letter-spacing:.5px}
.newsletter{position:absolute;left:678px;top:97px;width:417px;height:37px;border:1px solid #555;border-radius:19px}
.newsletter .ph{position:absolute;left:18px;top:9px;font-size:15px;color:#666;letter-spacing:.5px}
.newsletter .join{position:absolute;right:2px;top:2px;width:95px;height:31px;border-radius:16px;background:var(--brand);color:#fff;font-weight:700;font-size:15px;display:flex;align-items:center;justify-content:center}
.foot-bar{position:absolute;left:0;top:2285px;width:1200px;height:50px;background:var(--foot-bar);text-align:center;font-size:10.5px;color:#222;padding-top:12px;line-height:15px;letter-spacing:.3px}
</style>
</head>
<body>
<div class="page">

  <header class="site-header">
    <div class="brand">
      <div class="brand-mark"></div>
      <div>
        <div class="brand-name">QUILLSTONE</div>
        <div class="brand-tag">the quillstone movers &amp; storage inc.</div>
      </div>
    </div>
    <nav class="main-nav">
      <a class="active">HOME</a>
      <a>SERVICES</a>
      <a>OFFICE</a>
      <a>CONTACT</a>
      <span class="nav-phone">
        <svg width="15" height="15" viewBox="0 0 24 24" fill="none" stroke="#333" stroke-width="1.6"><circle cx="12" cy="12" r="11"/><path d="M8 6l2 3-1.3 1.5a8 8 0 0 0 4.8 4.8L15 14l3 2-1 2.2c-5 .2-10-4.8-9.8-9.8z"/></svg>
        (555) 014-2290
      </span>
    </nav>
    <a class="btn-request">REQUEST QUOTE</a>
  </header>

  <div class="hero-photo" role="img" aria-label="White moving truck parked on a residential street in front of a brick house and trees"></div>

  <form class="quote-panel">
    <div class="quote-title">I AM MOVING MY</div>
    <div class="tabs"><span>HOME</span><span>OFFICE</span><span>STORAGE</span></div>
    <div class="field" style="left:19px;top:54px"><label>Full name:</label><div class="input">Enter your full name</div></div>
    <div class="field" style="left:269px;top:54px"><label>Phone number:</label><div class="input">Enter your phone number</div></div>
    <div class="field" style="left:518px;top:54px"><label>Email:</label><div class="input">Enter your email</div></div>
    <div class="field" style="left:18px;top:105px"><label>Moving date:</label><div class="input">Select a date</div></div>
    <div class="field" style="left:269px;top:105px"><label>Moving from:</label><div class="input">Enter ZIP code</div></div>
    <div class="field" style="left:518px;top:105px"><label>Moving to:</label><div class="input">Enter ZIP code</div></div>
    <div class="truck-icon" role="img" aria-label="Small illustration of movers carrying boxes to a truck" style="background:linear-gradient(90deg,#d9c2a0,#3b2b22)"></div>
    <a class="btn-quote">GET QUOTE</a>
  </form>

  <h2 class="section-title" style="left:85px;top:628px">MOVING SERVICES</h2>

  <svg class="round-arrow" style="left:86px;top:775px" viewBox="0 0 34 34"><circle cx="17" cy="17" r="16" fill="#fff" stroke="#222" stroke-width="1.2"/><path d="M25 17H10M15 11l-6 6 6 6" fill="none" stroke="#222" stroke-width="1.5"/></svg>

  <article class="service-card featured" style="left:143px">
    <div class="photo" role="img" aria-label="Moving truck in front of a building" style="background:linear-gradient(160deg,#5a6a5e,#2c332d)"></div>
    <div class="featured-body">
      <h3>RESIDENTIAL MOVING</h3>
      <p>Lorem IpsumWe are the residential movers who strive to make your relocation experience simplified – regardless of whether you are moving across the street or across the country.</p>
      <div class="more"><span>Learn more</span><svg width="18" height="8" viewBox="0 0 18 8"><path d="M0 4h16M13 1l3 3-3 3" fill="none" stroke="#fff"/></svg></div>
    </div>
  </article>
  <article class="service-card" style="left:373px">
    <div class="photo" role="img" aria-label="Mover in a company shirt walking through an office" style="background:linear-gradient(160deg,#d8dde2,#8d949c)"></div>
    <div class="label">COMMERCIAL MOVING</div>
  </article>
  <article class="service-card" style="left:603px">
    <div class="photo" role="img" aria-label="Senior couple sitting on a bench outside a brick house" style="background:linear-gradient(160deg,#a8604a,#bfc6c9 60%,#7f8a6a)"></div>
    <div class="label">SENIOR MOVING</div>
  </article>
  <article class="service-card" style="left:833px">
    <div class="photo" role="img" aria-label="Warehouse aisle lined with wooden storage vaults" style="background:linear-gradient(90deg,#8a4f22,#c78a4a 50%,#8a4f22)"></div>
    <div class="label">STORAGE</div>
  </article>

  <svg class="round-arrow" style="left:1068px;top:775px" viewBox="0 0 34 34"><circle cx="17" cy="17" r="16" fill="#fff" stroke="#222" stroke-width="1.2"/><path d="M9 17h15M19 11l6 6-6 6" fill="none" stroke="#222" stroke-width="1.5"/></svg>

  <a class="btn-outline">View all services</a>

  <h2 class="section-title" style="left:86px;top:1016px">GET MOVED WITH PELDRAN MOVING SOLUTIONS!</h2>

  <section class="about-box">
    <ul class="about-list">
      <li><svg width="32" height="30" viewBox="0 0 24 23"><path fill="var(--star)" d="M12 0l3.5 7.6 8.3.9-6.2 5.6 1.8 8.2L12 18.1 4.6 22.3l1.8-8.2L.2 8.5l8.3-.9z"/></svg><p>We’re a stress-free moving company. Our goal is to get you moved easily efficiently.</p></li>
      <li><svg width="32" height="30" viewBox="0 0 24 23"><path fill="var(--star)" d="M12 0l3.5 7.6 8.3.9-6.2 5.6 1.8 8.2L12 18.1 4.6 22.3l1.8-8.2L.2 8.5l8.3-.9z"/></svg><p>Our reliable local movers live in the communities they serve. We’re not just your movers, we’re your neighbors.</p></li>
      <li><svg width="32" height="30" viewBox="0 0 24 23"><path fill="var(--star)" d="M12 0l3.5 7.6 8.3.9-6.2 5.6 1.8 8.2L12 18.1 4.6 22.3l1.8-8.2L.2 8.5l8.3-.9z"/></svg><p>We can handle any job, from one-room apartments to expansive estates.</p></li>
      <li><svg width="32" height="30" viewBox="0 0 24 23"><path fill="var(--star)" d="M12 0l3.5 7.6 8.3.9-6.2 5.6 1.8 8.2L12 18.1 4.6 22.3l1.8-8.2L.2 8.5l8.3-.9z"/></svg><p>Our team offers you convenient and affordable options for a completely stress-free experience.</p></li>
      <li><svg width="32" height="30" viewBox="0 0 24 23"><path fill="var(--star)" d="M12 0l3.5 7.6 8.3.9-6.2 5.6 1.8 8.2L12 18.1 4.6 22.3l1.8-8.2L.2 8.5l8.3-.9z"/></svg><p>As an agent of Peldran Van Lines, we can get you moved across town, across the country, or around the world.</p></li>
      <li><svg width="32" height="30" viewBox="0 0 24 23"><path fill="var(--star)" d="M12 0l3.5 7.6 8.3.9-6.2 5.6 1.8 8.2L12 18.1 4.6 22.3l1.8-8.2L.2 8.5l8.3-.9z"/></svg><p>Our trained, professional movers undergo rigorous background checks to maintain quality.</p></li>
    </ul>
    <a class="about-link">LEARN MORE ABOUT US→</a>
    <div class="pinned">
      <svg class="pin" style="left:2px" viewBox="0 0 12 16"><circle cx="7" cy="5" r="4" fill="#2f4fa8"/><path d="M6 8L2 15" stroke="#555" stroke-width="1.2"/></svg>
      <svg class="pin" style="right:8px" viewBox="0 0 12 16"><circle cx="7" cy="5" r="4" fill="#2f4fa8"/><path d="M6 8L2 15" stroke="#555" stroke-width="1.2"/></svg>
      <div class="photo" role="img" aria-label="Couple relaxing on a sofa among stacked moving boxes"></div>
    </div>
  </section>

  <section class="testimonials">
    <h2 class="section-title" style="left:87px;top:40px">TESTIMONIALS</h2>
    <svg class="dark-arrow" style="left:88px;top:193px" viewBox="0 0 34 34"><circle cx="17" cy="17" r="17" fill="#555"/><path d="M25 17H10M15 11l-6 6 6 6" fill="none" stroke="#fff" stroke-width="1.5"/></svg>

    <article class="t-card" style="left:172px">
      <div class="t-quote" style="left:20px;top:-10px">“</div>
      <div class="t-stars">
        <svg width="66" height="13" viewBox="0 0 66 13"><g fill="var(--star)"><path id="s" d="M6.5 0l1.9 4.1 4.5.5-3.4 3 1 4.5-4-2.3-4 2.3 1-4.5-3.4-3 4.5-.5z"/><use href="#s" x="13.3"/><use href="#s" x="26.6"/><use href="#s" x="39.9"/><use href="#s" x="53.2"/></g></svg>
      </div>
      <p class="t-text">Lorem ipsum dolor sit amet, consectetur adipiscing elit, sed do eiusmod tempor incididunt ut labore et dolore magna aliqua. Ut enim ad minim veniam, quis nostrud exercitation ullamco laboris nisi ut aliquip ex ea commodo consequat.</p>
      <div class="t-name">MARA QUINLEY</div>
      <div class="t-role">Happy client</div>
      <div class="t-quote" style="right:20px;top:175px">”</div>
    </article>

    <article class="t-card" style="left:635px">
      <div class="t-quote" style="left:20px;top:-10px">“</div>
      <div class="t-stars">
        <svg width="66" height="13" viewBox="0 0 66 13"><g fill="var(--star)"><use href="#s"/><use href="#s" x="13.3"/><use href="#s" x="26.6"/><use href="#s" x="39.9"/><use href="#s" x="53.2"/></g></svg>
      </div>
      <p class="t-text">Lorem ipsum dolor sit amet, consectetur adipiscing elit, sed do eiusmod tempor incididunt ut labore et dolore magna aliqua. Ut enim ad minim veniam, quis nostrud exercitation ullamco laboris nisi ut aliquip ex ea commodo consequat.</p>
      <div class="t-name">MARA QUINLEY</div>
      <div class="t-role">Happy client</div>
      <div class="t-quote" style="right:20px;top:175px">”</div>
    </article>

    <svg class="dark-arrow" style="left:1065px;top:193px" viewBox="0 0 34 34"><circle cx="17" cy="17" r="17" fill="#555"/><path d="M9 17h15M19 11l6 6-6 6" fill="none" stroke="#fff" stroke-width="1.5"/></svg>
  </section>

  <section class="cta">
    <h2>IS YOUR MOVE RIGHT AROUND THE CORNER?</h2>
    <a class="btn-white">GET A FREE QUOTE TODAY</a>
  </section>

  <footer class="site-footer">
    <div class="foot-brand"><div class="brand-mark"></div><div class="brand-name">QUILLSTONE</div></div>
    <div class="foot-company">The Quillstone Movers and Storage</div>
    <address class="foot-address" style="font-style:normal">418 Harbor Mill Rd,<br>Dunmere, CT 06999<br>Connecticut: 555-014-2290<br>Michigan: 555-018-4471</address>
    <ul class="foot-nav">
      <li>HOME</li><li>SERVICES</li><li>CONTACT</li><li>CEREER</li><li>GET QUOTE</li>
    </ul>
    <div class="foot-news-title">STAY IN TOUCH WITH QUILLSTONE</div>
    <div class="foot-news-text">Join our mailing list to stay up to date on our last news</div>
    <div class="newsletter"><span class="ph">Enter email address</span><span class="join">Join</span></div>
  </footer>

  <div class="foot-bar">Privacy Policy · Site Map · Page Top<br>© 2022. All Rights Reserved. The Quillstone Movers and Storage</div>

</div>
</body>
</html>
```